Brookvale Urgent Care Clinic
Business card and stationary
Brookvale Urgent Care Clinic - Health
Creative Brief
Professional
2847 Quarrow Blvd, Suite 316 Dallas, Texas 75214
wolcastry@mailbrisk.com
www.BrookvaleUC.com
I only want the company name, physicial address and web site on the front with a design. On back only black and white map.
Black and white map of location

```html
<!DOCTYPE html>
<html lang="en">
<head>
<meta charset="utf-8">
<title>Brookvale Urgent Care Clinic – Stationery</title>
<link href="https://fonts.googleapis.com/css2?family=Cinzel:wght@600&family=Open+Sans:wght@400;600&display=swap" rel="stylesheet">
<style>
  :root {
    --board: #6e4526;
    --board-dark: #5a371d;
    --paper: #ffffff;
    --brand-red: #b3161b;
    --brand-red-dark: #7d0d10;
    --ink: #555555;
    --ink-soft: #8c8c8c;
    --band-light: #f2f2f2;
    --band-dark: #7a7a7a;
    --rule: #c9c9c9;
  }
  * { box-sizing: border-box; margin: 0; padding: 0; }
  html, body { width: 1200px; height: 511px; overflow: hidden; }
  body {
    background: radial-gradient(circle at 50% 45%, var(--board) 0%, var(--board-dark) 100%);
    font-family: "Open Sans", Arial, sans-serif;
    color: var(--ink);
    position: relative;
  }
  .sheet, .envelope, .card {
    position: absolute;
    background: var(--paper);
    box-shadow: 2px 3px 6px rgba(0,0,0,.35);
    overflow: hidden;
  }
  .side-band {
    position: absolute; left: 0; top: 0; bottom: 0;
    background: linear-gradient(to bottom, var(--band-light) 0%, var(--band-dark) 55%, var(--band-light) 100%);
  }
  .brand { position: absolute; display: flex; align-items: center; gap: 6px; }
  .brand-dot {
    border-radius: 50%;
    background: var(--brand-red);
    flex: none;
  }
  .brand-name {
    font-family: "Cinzel", Georgia, serif;
    font-weight: 600;
    color: var(--brand-red);
    line-height: 1.05;
    letter-spacing: .02em;
  }
  .faint-circle {
    position: absolute; border-radius: 50%;
    background: rgba(0,0,0,.035);
  }
  .contact {
    position: absolute; font-size: 4.5px; line-height: 1.45; color: var(--ink);
  }
  .web {
    position: absolute; font-size: 5px; color: var(--ink); font-weight: 600;
  }

  /* letterhead */
  .letterhead { left: 22px; top: 72px; width: 322px; height: 420px; }
  .letterhead .side-band { width: 26px; }
  .letterhead .brand { left: 34px; top: 40px; }
  .letterhead .brand-dot { width: 24px; height: 24px; }
  .letterhead .brand-name { font-size: 12px; }
  .letterhead .contact { left: 200px; top: 42px; }
  .letterhead .faint-circle { width: 170px; height: 170px; right: -30px; top: 170px; }
  .letterhead .web { right: 14px; bottom: 12px; }

  /* fax */
  .fax { left: 372px; top: 72px; width: 322px; height: 420px; }
  .fax .side-band { width: 26px; }
  .fax .brand { left: 34px; top: 40px; }
  .fax .brand-dot { width: 24px; height: 24px; }
  .fax .brand-name { font-size: 12px; }
  .fax .contact { left: 200px; top: 42px; }
  .fax .web { right: 14px; bottom: 12px; }
  .fax-title {
    position: absolute; left: 40px; top: 96px;
    font-size: 20px; line-height: .95; color: #333; font-weight: 400;
  }
  .fax-fields {
    position: absolute; left: 40px; top: 150px; width: 270px;
    display: grid; grid-template-columns: 1fr 1fr; column-gap: 14px; row-gap: 6px;
    font-size: 5px;
  }
  .fax-field { border-bottom: 1px solid var(--rule); padding-bottom: 2px; }
  .fax-field.header-row { border-bottom: none; }
  .fax-rule { position: absolute; left: 40px; width: 270px; height: 1px; background: var(--rule); }
  .fax-checks {
    position: absolute; left: 40px; top: 206px; width: 270px;
    display: flex; justify-content: space-between; font-size: 4.5px;
  }
  .fax-check { display: flex; gap: 3px; align-items: flex-start; }
  .fax-check .box { width: 6px; height: 6px; border: 1px solid #888; flex: none; }

  /* envelopes */
  .envelope-back { left: 732px; top: 34px; width: 440px; height: 192px; }
  .envelope-back svg { position: absolute; left: 0; top: 0; }
  .envelope-front { left: 732px; top: 168px; width: 428px; height: 178px; }
  .envelope-front .side-band { width: 30px; }
  .envelope-front .brand { left: 40px; top: 20px; }
  .envelope-front .brand-dot { width: 24px; height: 24px; }
  .envelope-front .brand-name { font-size: 12px; }
  .envelope-front .contact { left: 40px; top: 64px; }
  .envelope-front .web { right: 14px; bottom: 10px; }

  /* business cards */
  .card-front { left: 782px; top: 354px; width: 74px; height: 42px; }
  .card-front .side-band { width: 6px; }
  .card-front .brand { left: 10px; top: 8px; gap: 3px; }
  .card-front .brand-dot { width: 9px; height: 9px; }
  .card-front .brand-name { font-size: 5px; }
  .card-front .web { right: 4px; bottom: 3px; font-size: 2.6px; }
  .card-back {
    left: 782px; top: 404px; width: 166px; height: 94px;
    background: linear-gradient(135deg, var(--brand-red) 0%, var(--brand-red-dark) 100%);
  }
  .card-map {
    position: absolute; left: 10px; top: 10px; width: 146px; height: 74px;
    background: linear-gradient(160deg, #c63a3e 0%, #a01216 100%);
    border: 1px solid rgba(255,255,255,.35);
  }
  .card-back .web { right: 8px; bottom: 6px; color: #fff; font-size: 4px; }
</style>
</head>
<body>

  <section class="sheet letterhead" aria-label="Letterhead">
    <div class="side-band"></div>
    <div class="brand"><span class="brand-dot"></span><span class="brand-name">Brookvale Urgent<br>Care Clinic</span></div>
    <div class="contact">2847 Quarrow Blvd, Suite 316<br>Dallas, Texas 75214<br>T 214.555.0187<br>wolcastry@mailbrisk.com</div>
    <div class="faint-circle"></div>
    <div class="web">www.BrookvaleUC.com</div>
  </section>

  <section class="sheet fax" aria-label="Fax cover sheet">
    <div class="side-band"></div>
    <div class="brand"><span class="brand-dot"></span><span class="brand-name">Brookvale Urgent<br>Care Clinic</span></div>
    <div class="contact">2847 Quarrow Blvd, Suite 316<br>Dallas, Texas 75214<br>T 214.555.0187<br>F 214.555.0188</div>
    <div class="fax-title">FA<br>X</div>
    <div class="fax-rule" style="top:142px"></div>
    <div class="fax-fields">
      <div class="fax-field">To:</div><div class="fax-field">From:</div>
      <div class="fax-field">Fax:</div><div class="fax-field">Pages:</div>
      <div class="fax-field">Phone:</div><div class="fax-field">Date:</div>
      <div class="fax-field">Re:</div><div class="fax-field">CC:</div>
    </div>
    <div class="fax-checks">
      <div class="fax-check"><span class="box"></span>Urgent</div>
      <div class="fax-check"><span class="box"></span>For<br>Review</div>
      <div class="fax-check"><span class="box"></span>Please<br>Comment</div>
      <div class="fax-check"><span class="box"></span>Please<br>Reply</div>
      <div class="fax-check"><span class="box"></span>Please<br>Recycle</div>
    </div>
    <div class="web">www.BrookvaleUC.com</div>
  </section>

  <section class="envelope envelope-back" aria-label="Envelope back">
    <svg width="440" height="192" viewBox="0 0 440 192">
      <defs>
        <linearGradient id="flapRed" x1="0" y1="0" x2="0" y2="1">
          <stop offset="0" stop-color="#c0191f"/>
          <stop offset="1" stop-color="#7d0d10"/>
        </linearGradient>
      </defs>
      <polyline points="0,192 220,70 440,192" fill="none" stroke="#d6d6d6" stroke-width="1"/>
      <path d="M0,0 H440 V34 L220,100 L0,34 Z" fill="url(#flapRed)"/>
      <circle cx="220" cy="46" r="15" fill="#ffffff"/>
      <circle cx="220" cy="46" r="12" fill="#b3161b"/>
    </svg>
  </section>

  <section class="envelope envelope-front" aria-label="Envelope front">
    <div class="side-band"></div>
    <div class="brand"><span class="brand-dot"></span><span class="brand-name">Brookvale Urgent<br>Care Clinic</span></div>
    <div class="contact">2847 Quarrow Blvd, Suite 316 Dallas, Texas 75214</div>
    <div class="web">www.BrookvaleUC.com</div>
  </section>

  <section class="card card-front" aria-label="Business card front">
    <div class="side-band"></div>
    <div class="brand"><span class="brand-dot"></span><span class="brand-name">Brookvale Urgent<br>Care Clinic</span></div>
    <div class="web">www.BrookvaleUC.com</div>
  </section>

  <section class="card card-back" aria-label="Business card back">
    <div class="card-map" role="img" aria-label="Street map showing the clinic location on Quarrow Blvd"></div>
    <div class="web">www.BrookvaleUC.com</div>
  </section>

</body>
</html>
```